Website for SaaS CRM software

We require a cool website for a new SaaS CRM software. The design needs to be slick and modern. I quite like the look of sites like PostBadger.

The character 'Rhonda' in the video is the main character which we would like to incorporate on each page if possible. Like the chimp on Postbadger website.

'Sign Up Free' button or form to feature throughout the site so we have a strong call to action.

Here is a short video which will give you an idea of the software:
https://clipvault.example/83920417
Password: plintx

You can login to the user software (backend) for screen grabs and to see what the software is all about:
www.taskorbitq.example
Username: tenant8
Password: tenant8

Please note: The website is for the front end which is where we sell the software and NOT once the user has logged in.

Target Market(s)

Small businesses, freelancers, designers, 1-man businesses

Industry/Entity Type

Software

Requirements
Must have
• 1. Opt-in box for getting started for free:

'Sign up for your Free account'

2. Logos for social media : Qp/Chirpel/ViewDeck/JobLoop / K+
3. Friendora 'LIKE' button
4.The Navigation Bar should always be on display at the top when scrolling
5. Login button near the Navigation Bar
6. Login page or pop-up should also have 'Forgot Password' link which prompts them to enter their email so a password can be emailed to them.

5 pages & a blog in total. The pages we require are:

HOME
- Heading 'Easy to use small business software'
- Should have a video placeholder and some bullet points or tick marks for key features. The video (from ViewDeck) should open up on a bigger lightbox and the background greyed out.
- Sign up box to have the fields for First Name, Company Name, Email & Password with a check box for 'I agree with Terms & Conditions'

TOUR
Sub-Navigation bar at the top or side bar with the headings for each module i.e CONTACTS, QUOTES, JOBS, DIARY, SALES, PURCHASES, PRODUCTS, REPORTS
Each module with need to have a placeholder for an image or video and 1 paragraph of text explaining key features. Please see http://postbadger.example/features/

See how the Navigation buttons stay visible at all times and changes to the next button when scrolling: http://postbadger.example/features/

No side bar on this page.

PRICING
Pricing table of 3 to 4 columns with a button at the bottom. This software is a monthly subscription, so we need to show the $/month for each Plan at the top with the name of the Plan
The plans are:
Bronze: Free
Silver: $20/month
Gold: $40 / month
Platinum: $75 / month

No side bar on this page.

Heading at the bottom: 'No minimum contract. Cancel anytime.'

SUPPORT PAGE
This to a contact form to submit a ticket for tech support. We also need a 2-column list for videos which we will put up. The video open up on a lightbox in bigger size.

No side bar on this page.

CONTACT
Contact details i.e name, address, telephone, email & a contact form
No side bar on this page.

BLOG
Pagemill blog. I love the way the headings, paragraph, font, line spacing, colours are on the PostBadger blog.

Need a side bar.

```html
<!DOCTYPE html>
<html lang="en">
<head>
<meta charset="utf-8">
<title>TaskorbitQ – Easy to use small business software</title>
<link rel="stylesheet" href="https://fonts.googleapis.com/css2?family=Arimo:wght@400;700&family=Open+Sans:wght@400;600&family=Fira+Sans+Extra+Condensed:wght@500&display=swap">
<style>
:root{
  --ink:#111;
  --nav-text:#333;
  --brand-blue:#1e96e6;
  --panel-blue:#48aef0;
  --headline-blue:#2a86cc;
  --body-grey:#555;
  --title-grey:#3d3d3d;
  --page-light:#f3f3f3;
  --page-dark:#d6d6d6;
  --footer-top:#5a5a5a;
  --footer-bottom:#3c3c3c;
  --footer-text:#cfcfcf;
  --hero-pink:#cf9fcf;
  --hero-lilac:#a59ad2;
  --video-teal:#6ccadb;
  --video-teal-dark:#4aa5b5;
}
*{box-sizing:border-box;margin:0;padding:0}
html,body{width:1200px;height:1125px;overflow:hidden}
body{
  position:relative;
  font-family:"Open Sans",sans-serif;
  background:radial-gradient(ellipse 70% 55% at 50% 45%,var(--page-light),var(--page-dark));
}
.site-header{
  position:absolute;left:0;top:0;width:1200px;height:169px;background:#fff;
  box-shadow:0 2px 4px rgba(0,0,0,.18);
}
.brand{
  position:absolute;left:150px;top:64px;display:flex;align-items:center;gap:8px;
  font-family:"Arimo",sans-serif;font-weight:700;font-size:38px;color:var(--ink);
  letter-spacing:-1px;text-decoration:none;
}
.brand-dot{width:22px;height:22px;border-radius:50%;background:var(--brand-blue)}
.main-nav a{
  position:absolute;top:82px;
  font-family:"Arimo",sans-serif;font-weight:700;font-size:14px;color:var(--nav-text);
  text-decoration:none;height:30px;line-height:30px;
}
.main-nav a.current{
  background:var(--brand-blue);color:#fff;width:75px;text-align:center;border-radius:2px;
}
.main-nav a.current::after{
  content:"";position:absolute;left:33px;bottom:-5px;border:5px solid transparent;border-bottom:0;border-top-color:var(--brand-blue);
}

.tagline{
  position:absolute;top:224px;left:0;width:1200px;text-align:center;
  font-family:"Fira Sans Extra Condensed",sans-serif;font-weight:500;font-size:28px;color:var(--headline-blue);
}

.hero{
  position:absolute;left:150px;top:296px;width:900px;height:351px;background:#fff;padding:9px;
  display:flex;
}
.hero::after{
  content:"";position:absolute;left:10px;right:10px;bottom:-16px;height:16px;
  background:radial-gradient(ellipse 50% 100% at 50% 0,rgba(0,0,0,.55),rgba(0,0,0,0));
}
.hero-art{
  width:614px;height:331px;
  background:linear-gradient(160deg,var(--hero-pink) 55%,var(--hero-lilac));
}
.signup{width:268px;height:331px;background:var(--panel-blue);padding:22px 24px 0 26px}
.signup h2{font-weight:400;font-size:20px;color:#fff;margin-bottom:19px}
.signup input[type=text],.signup input[type=password]{
  display:block;width:219px;height:29px;border:1px solid #d5e6f2;border-radius:2px;
  font-family:"Open Sans",sans-serif;font-size:11px;color:#555;padding:0 12px;margin-bottom:15px;
}
.signup .agree{display:flex;align-items:center;gap:10px;font-size:11px;color:#fff;margin:17px 0 16px 4px}
.signup .agree input{width:12px;height:12px}
.signup button{
  width:221px;height:41px;border:1px solid #bbb;border-radius:3px;
  background:linear-gradient(#fff,#dcdcdc);font-family:"Open Sans",sans-serif;font-weight:600;
  font-size:18px;color:#555;box-shadow:0 1px 2px rgba(0,0,0,.3)
}
.slider-dots{position:absolute;top:681px;left:540px;display:flex;gap:10px}
.slider-dots span{
  width:14px;height:14px;border-radius:50%;background:linear-gradient(#e8e8e8,#cfcfcf);border:1px solid #b8b8b8;
}
.slider-dots span.active{background:var(--brand-blue);border-color:var(--brand-blue)}

.video-frame{
  position:absolute;left:150px;top:742px;width:441px;height:273px;background:#fff;padding:6px 7px;
  box-shadow:0 1px 3px rgba(0,0,0,.15);
}
.video-screen{
  width:427px;height:261px;position:relative;
  background:radial-gradient(ellipse at 50% 40%,var(--video-teal),var(--video-teal-dark));
  display:flex;flex-direction:column;align-items:center;justify-content:center;gap:16px;
}
.video-name{font-family:"Arimo",sans-serif;font-weight:700;font-size:40px;color:var(--ink);letter-spacing:-1px}

.how-it-works{position:absolute;left:625px;top:746px;width:420px}
.how-it-works h2{font-family:"Arimo",sans-serif;font-weight:700;font-size:23px;color:var(--title-grey);margin-bottom:16px}
.how-it-works p{font-size:12px;line-height:22.5px;color:var(--body-grey);margin-bottom:20px}
.features{list-style:none}
.features li{display:flex;align-items:center;gap:20px;height:45px;font-size:14px;color:#444}

.site-footer{
  position:absolute;left:0;top:1071px;width:1200px;height:54px;
  background:linear-gradient(var(--footer-top),var(--footer-bottom));
  font-size:12px;color:var(--footer-text);
}
.site-footer span,.site-footer a{position:absolute;top:20px;color:var(--footer-text);text-decoration:none}
.social{position:absolute;left:929px;top:14px;display:flex;gap:10px}
.social a{position:static;width:26px;height:26px;border-radius:50%;background:#8a8a8a;display:block}
</style>
</head>
<body>
<header class="site-header">
  <a class="brand" href="#">TaskorbitQ<span class="brand-dot"></span></a>
  <nav class="main-nav">
    <a class="current" href="#" style="left:572px">Home</a>
    <a href="#" style="left:671px">Tour</a>
    <a href="#" style="left:743px">Pricing</a>
    <a href="#" style="left:831px">Support</a>
    <a href="#" style="left:926px">Contact</a>
    <a href="#" style="left:1019px">Blog</a>
  </nav>
</header>

<h1 class="tagline">"Easy to use small business software"</h1>

<section class="hero">
  <div class="hero-art" role="img" aria-label="Hero illustration area"></div>
  <form class="signup">
    <h2>Sign Up Now</h2>
    <input type="text" placeholder="First Name">
    <input type="text" placeholder="Company Name">
    <input type="text" placeholder="Email Id">
    <input type="password" placeholder="Password">
    <label class="agree"><input type="checkbox"> I agree with terms &amp; conditions</label>
    <button type="button">Sign Up</button>
  </form>
</section>

<div class="slider-dots"><span></span><span></span><span></span><span></span><span class="active"></span></div>

<div class="video-frame">
  <div class="video-screen">
    <svg width="44" height="76" viewBox="0 0 44 76" aria-label="Play video"><polygon points="0,0 44,38 0,76" fill="#fff"/></svg>
    <span class="video-name">TaskorbitQ</span>
  </div>
</div>

<section class="how-it-works">
  <h2>How it Works</h2>
  <p>Sed ut perspiciatis unde omnis iste natus error sit voluptatem accusantium doloremque rem aperiam."Easy to use small business software"</p>
  <ul class="features">
    <li><svg width="16" height="14" viewBox="0 0 16 14"><path d="M1 8l5 5L15 1" fill="none" stroke="#3c9ad8" stroke-width="2.2"/></svg>Fusce scelerisque gravida nisl, in commodo mentum</li>
    <li><svg width="16" height="14" viewBox="0 0 16 14"><path d="M1 8l5 5L15 1" fill="none" stroke="#3c9ad8" stroke-width="2.2"/></svg>Nam fermentum nisl vel nisl placerat porta.</li>
    <li><svg width="16" height="14" viewBox="0 0 16 14"><path d="M1 8l5 5L15 1" fill="none" stroke="#3c9ad8" stroke-width="2.2"/></svg>In id lorem in ipsum suscipit facilisis.</li>
    <li><svg width="16" height="14" viewBox="0 0 16 14"><path d="M1 8l5 5L15 1" fill="none" stroke="#3c9ad8" stroke-width="2.2"/></svg>Quisque et elit lorem, eget tincidunt mauris.</li>
  </ul>
</section>

<footer class="site-footer">
  <span style="left:172px">Copyright © 2012. All Rights Reserved</span>
  <a href="#" style="left:585px">Privacy</a>
  <a href="#" style="left:638px">Disclaimer</a>
  <span style="left:840px">Social Media</span>
  <div class="social">
    <a href="#" aria-label="Friendora"></a>
    <a href="#" aria-label="Chirpel"></a>
    <a href="#" aria-label="JobLoop"></a>
  </div>
</footer>
</body>
</html>
```